VelmaraStitch.com will be an online bespoke garment creator, specifically around designing your own Wedding Dress. It will enable you to specify your own material, colours and patterns and customized features such as bows, sequins, diamantes, and more from a selection of per-defined base garments and customize them to your taste.
The concept is similar to:
www.theorvandlane.example
But the design should reflect more like
www.quillbarn.example
www.dunwel.example - (in particular the build elements)
www.tarvo.example
It will be aimed at the Female marketplace. However this does not mean to use pink or portray the brand in very girly way. It should use good white space, and look very classy. not too busy, but functional and elegant, with a focus on stable and responsible site that will deliver. A wedding dress is an important purchase and to trust a company to make one for you from a distance takes a lot of trust from the customer perspective.
We want to first create the homepage and "build the dress" pages, which will consist of Enter your Measurements, Choose a Base Silhouette Style, Choose Fabric, Choose Colors, Customize Dress, Summary, Order Page, Thank you Page.
It will then have generic About us, How to Measure, Agent Locator, How it works, Contact, Order Samples, Support.
A very basic wire frame was created here to aid development, but the branding is being developed, so do not use any of it for inspiration just a visual interpretation - http://pexlarnode.example/velmara/
The link above is merely an idea on what areas the site will have. The actual design and colour scheme should reflect these sites.
The branding is also here - www.velmarastitch.example not the one used within that link.
The site will enable you to log in, save your designs and your delivery and measurement information. It will also offer the usual social media buttons to share the design and ability to leave comments.
This will be the first draft and the winning design will get to design the other pages and future work associated to the site.
thanks!

```html
<!DOCTYPE html>
<html lang="en">
<head>
<meta charset="utf-8">
<title>VelmaraStitch – Home</title>
<link href="https://fonts.googleapis.com/css2?family=Arimo&family=Cinzel:wght@500;600&family=Open+Sans:wght@400;600&family=PT+Sans+Narrow&display=swap" rel="stylesheet">
<style>
:root{
  --ink:#1a1a1a;
  --text:#333;
  --muted:#777;
  --faint:#999;
  --rule:#444;
  --black:#000;
  --white:#fff;
  --btn:#6d6d6d;
  --caption:rgba(78,78,80,.86);
}
*{margin:0;padding:0;box-sizing:border-box}
html,body{width:1200px;height:1200px;overflow:hidden;background:var(--white)}
body{position:relative;font-family:"Arimo",Arial,sans-serif;color:var(--text)}
a{color:inherit;text-decoration:none}
.abs{position:absolute}
.util{top:32px;font-size:12px;color:var(--muted);letter-spacing:.3px}
.util span{margin:0 12px;color:var(--muted)}
.rule{position:absolute;left:100px;width:1001px;height:1px;background:var(--rule)}
.nav a{position:absolute;top:85px;font-family:"PT Sans Narrow",sans-serif;font-size:16.5px;color:var(--ink);text-transform:uppercase}
.brand{left:441px;top:24px;width:318px;height:95px;background:var(--black);display:flex;align-items:center}
.brand-mark{width:84px;height:84px;border-radius:50%;border:4px solid var(--white);margin-left:29px}
.brand-name{margin-left:13px;color:var(--white);font-family:"Cinzel",serif;font-size:14px;letter-spacing:3.2px}
.hero-frame{left:99px;top:139px;width:1002px;height:484px;border:1px solid var(--ink)}
.hero-photo{left:113px;top:153px;width:974px;height:456px;background:linear-gradient(180deg,#6b5d55 0%,#8a7a6c 30%,#c9b8a4 55%,#7d7f8c 72%,#2f4f9c 100%)}
.hero-caption{left:113px;top:488px;width:974px;height:121px;background:var(--caption);color:var(--white);font-family:"Open Sans",sans-serif;overflow:hidden}
.hero-caption h1{position:absolute;left:20px;top:6px;font-weight:400;font-size:34px;white-space:nowrap}
.hero-caption p{position:absolute;left:23px;top:62px;width:940px;font-size:15.5px;line-height:22px;letter-spacing:-.1px}
.hero-caption u{font-weight:600;margin-left:12px;white-space:nowrap}
.arrow{top:369px;width:30px;height:30px;background:rgba(210,210,210,.8);display:flex;align-items:center;justify-content:center}
.feature h2{font-family:"PT Sans Narrow",sans-serif;font-weight:400;font-size:24px;line-height:26px;color:var(--ink);display:flex;align-items:center;gap:10px;white-space:nowrap}
.feature .dot{display:inline-block;width:17px;height:17px;border:1px solid #bbb;border-radius:50%}
.feature p{font-size:12px;line-height:20px;margin-top:3px;color:var(--ink);letter-spacing:.2px;white-space:nowrap}
.feature .more{display:block;margin-top:11px;font-size:12px;color:var(--faint);text-decoration:underline}
.build{left:859px;top:645px;width:225px;height:164px;border:1px solid var(--ink)}
.build span{position:absolute;left:13px;top:53px;font-family:"PT Sans Narrow",sans-serif;font-size:26px;line-height:31px;color:var(--ink)}
.build .figure{position:absolute;left:88px;top:12px;width:118px;height:140px;background:linear-gradient(180deg,#f4f4f4,#e4e4e4)}
.section-head{font-family:"Cinzel",serif;font-weight:600;font-size:14.5px;color:var(--ink);text-align:center;white-space:nowrap}
.email{left:243px;top:919px;width:211px;height:25px;border:1px solid #ccc;font-family:Georgia,serif;font-size:13px;color:var(--faint);padding:4px 13px}
.go{left:454px;top:919px;width:53px;height:25px;background:var(--btn);color:var(--white);font-family:"Cinzel",serif;font-weight:600;font-size:14px;text-align:center;line-height:25px}
.social{top:921px;height:20px;border:1px solid #bbb;border-radius:3px;font-size:12px;line-height:18px;padding:0 6px}
.follow{left:790px;background:var(--btn);color:var(--white);border-color:var(--btn)}
.like{left:864px;background:#f0f0f0;color:#335}
.count{left:913px;top:922px;width:24px;height:19px;border:1px solid #ccc}
.links{top:992px;font-size:12px;line-height:24px;color:var(--ink);list-style:none;letter-spacing:.3px}
.legal{top:1155px;font-size:12px;color:var(--faint);letter-spacing:.2px;white-space:nowrap}
.legal a{margin-right:15px}
</style>
</head>
<body>
<header>
  <div class="abs util" style="left:107px">Login<span>|</span>New User Register here</div>
  <div class="abs util" style="left:958px">Contact Us<span>|</span>My Order</div>
  <div class="rule" style="top:71px"></div>
  <div class="rule" style="top:118px"></div>
  <nav class="nav">
    <a style="left:110px">About Us</a>
    <a style="left:198px">How to Measure</a>
    <a style="left:334px">Agent Locator</a>
    <a style="left:773px">How it Works</a>
    <a style="left:898px">Order Samples</a>
    <a style="left:1026px">Support</a>
  </nav>
  <div class="abs brand"><div class="brand-mark"></div><div class="brand-name">VELMARASTITCH</div></div>
</header>

<section>
  <div class="abs hero-frame"></div>
  <div class="abs hero-photo" role="img" aria-label="Bride in a white strapless dress with bridesmaids in blue dresses holding white flowers"></div>
  <div class="abs arrow" style="left:113px"><svg width="10" height="12"><path d="M7 1 2 6l5 5" stroke="#222" stroke-width="2.5" fill="none"/></svg></div>
  <div class="abs arrow" style="left:1057px"><svg width="10" height="12"><path d="M3 1l5 5-5 5" stroke="#222" stroke-width="2.5" fill="none"/></svg></div>
  <div class="abs hero-caption">
    <h1>Looking for Wedding Dress?</h1>
    <p>VelmaraStitch an online bespoke garment creator, which provide you complete customise solutions to get your wedding dress like choose your own material, colours and patterns and many other customized features.<u>Click here for more details</u></p>
  </div>
</section>

<section>
  <div class="abs feature" style="left:115px;top:645px">
    <h2>HOW TO MEASURE <i class="dot"></i></h2>
    <p>some lorem ipsum text will be here<br>some lorem ipsum text will be here<br>some lorem ipsum text will be here<br>some lorem ipsum text will be here<br>some lorem ipsum text will be here</p>
    <a class="more" style="margin-left:-1px">read more</a>
  </div>
  <div class="abs feature" style="left:363px;top:645px">
    <h2>AGENT LOCATOR <i class="dot" style="margin-left:10px"></i></h2>
    <p>some lorem ipsum text will be here<br>some lorem ipsum text will be here<br>some lorem ipsum text will be here<br>some lorem ipsum text will be here<br>some lorem ipsum text will be here</p>
    <a class="more" style="margin-left:-1px">read more</a>
  </div>
  <div class="abs feature" style="left:613px;top:645px">
    <h2>HOW IT WORKS <i class="dot" style="margin-left:22px"></i></h2>
    <p>some lorem ipsum text will be here<br>some lorem ipsum text will be here<br>some lorem ipsum text will be here<br>some lorem ipsum text will be here<br>some lorem ipsum text will be here</p>
    <a class="more" style="margin-left:-1px">read more</a>
  </div>
  <div class="abs build">
    <div class="figure" role="img" aria-label="Line sketch of a woman in a full-skirted gown"></div>
    <span>BUILD YOUR<br>DRESS</span>
  </div>
</section>

<section>
  <div class="rule" style="top:860px"></div>
  <div class="abs" style="left:597px;top:874px;width:1px;height:77px;background:var(--ink)"></div>
  <div class="abs section-head" style="left:200px;top:890px;width:334px">JOIN OUR NEWSLETTER</div>
  <div class="abs email">enter email</div>
  <div class="abs go">GO</div>
  <div class="abs section-head" style="left:660px;top:890px;width:420px">FOLLOW US AND GET TO KOW US BETTER</div>
  <div class="abs social follow">+ Follow</div>
  <div class="abs social like">Like</div>
  <div class="abs count"></div>
  <div class="rule" style="top:971px"></div>
</section>

<footer>
  <ul class="abs links" style="left:108px"><li>About Us</li><li>Our Company</li><li>Our Mission</li><li>Contact Us</li><li>Privacy policy</li></ul>
  <ul class="abs links" style="left:329px"><li>About Us</li><li>Our Company</li><li>Our Mission</li><li>Contact Us</li><li>Privacy policy</li></ul>
  <ul class="abs links" style="left:540px"><li>About Us</li><li>Our Company</li><li>Our Mission</li><li>Contact Us</li><li>Privacy policy</li></ul>
  <ul class="abs links" style="left:751px"><li>About Us</li><li>Our Company</li><li>Our Mission</li><li>Contact Us</li><li>Privacy policy</li></ul>
  <ul class="abs links" style="left:952px"><li>About Us</li><li>Our Company</li><li>Our Mission</li><li>Contact Us</li><li>Privacy policy</li></ul>
  <div class="rule" style="top:1132px"></div>
  <div class="abs legal" style="left:104px"><a>Terms &amp; conditions</a><a>Privacy policy</a><a>Sitemap</a></div>
  <div class="abs legal" style="right:108px">VelmaraStitch, Harlow Court, Brennick, 480213, info@velmarastitch.example</div>
</footer>
</body>
</html>
```